Business is called "Kestrel Ledger". Accounting and tax services.

I need a flyer for my new business "Kestrel Ledger". I am an individual accountant working for himself on the Sunshine Coast in Queensland Australia. I would like to see designs that communicate reliability and trust. I believe my point of difference is that I am always available to my clients and I will cap my number of clients to ensure I can service them properly. Accountants in general seem to have a bad reputation for not responding to clients in a timely fashion, whether by email or phone. This is where I intend to differentiate myself. I have included my business card for ideas on colour and for contact information. I have also included some logo's that should go on the flyer. With the QLA logo, the words "Kestrel Ledger is a QLA Business" needs to be written either above, below or to the right hand side (as per the business card).

Target Market(s)

Small business owners and individuals requiring taxation and financials

Industry/Entity Type

Public Accounting

Font styles to use
Serif

Requirements
Must have
• Supplied logo's, accounting style pictures etc
Services: Small Business Taxation
Company & Trust Tax Returns
Rental Property Returns
Capital Gains Tax
Individual Tax Returns
BAS and IAS lodgements
Nice to have
• Needs to convey a sense of being reliable and responds to clients quickly.
Should not have
• My name

```html
<!DOCTYPE html>
<html lang="en">
<head>
<meta charset="utf-8">
<title>Kestrel Ledger – Services Flyer</title>
<link rel="stylesheet" href="https://fonts.googleapis.com/css2?family=Montserrat:wght@400;500;600;700&display=swap">
<style>
  :root{
    --ink:#2b2b2b;
    --teal:#17b390;
    --teal-dark:#22a580;
    --white:#ffffff;
    --purple:#9b3d97;
    --pink:#ec1f86;
    --olive:#8b9a3c;
    --indigo:#55479e;
    --royal:#2f4fa2;
    --green:#45b649;
    --qla-blue:#1a5aa8;
    --badge-grey:#cfcfcf;
    --app-cyan:#1fb3e8;
  }
  *{margin:0;padding:0;box-sizing:border-box}
  html,body{width:849px;height:1200px;overflow:hidden;background:var(--white)}
  body{font-family:"Montserrat",sans-serif;color:var(--ink)}
  .flyer{position:relative;width:849px;height:1200px;overflow:hidden;background:var(--white)}

  .hero-photo{
    position:absolute;left:0;top:0;width:849px;height:545px;
    background:
      radial-gradient(ellipse at 75% 15%, rgba(230,190,120,.35), transparent 40%),
      linear-gradient(165deg,#c4d3e0 0%,#e9eef4 45%,#f3f5f8 70%,#dde5ee 100%);
  }
  .brand-ring{position:absolute;left:165px;top:211px;width:146px;height:146px;border:3px solid var(--ink);border-radius:50%}
  .brand-name{
    position:absolute;left:42px;top:383px;
    font-size:30px;font-weight:500;letter-spacing:.26em;color:var(--ink);white-space:nowrap;
  }

  .services-band{
    position:absolute;left:0;top:539px;width:849px;height:64px;
    background:var(--teal);border-top-right-radius:44px;
  }
  .services-title{position:absolute;left:94px;top:14px;font-size:29px;font-weight:600;color:var(--white)}
  .services-rule{position:absolute;left:236px;top:44px;width:579px;height:1.5px;background:var(--white)}

  .service{position:absolute;width:260px;text-align:center}
  .service-icon{display:block;margin:0 auto;width:114px;height:114px}
  .service-label{margin-top:20px;font-size:16.5px;font-weight:500;color:var(--ink);white-space:nowrap}

  .footer-rule{position:absolute;left:0;top:1087px;width:530px;height:1.5px;background:var(--teal-dark)}
  .member-tab{
    position:absolute;left:548px;top:1068px;width:301px;height:40px;
    background:var(--teal-dark);border-radius:20px 0 0 20px;
    color:var(--white);font-size:15.5px;font-weight:500;line-height:40px;padding-left:16px;white-space:nowrap;
  }

  .qla-mark{position:absolute;left:42px;top:1121px;display:flex;align-items:center;gap:10px}
  .qla-square{width:56px;height:56px;background:var(--qla-blue)}
  .qla-name{font-size:30px;font-weight:500;color:var(--qla-blue)}
  .registered-badge{position:absolute;left:210px;top:1124px;width:48px;height:48px;border-radius:50%;background:var(--badge-grey)}
  .app-partner{position:absolute;left:275px;top:1138px;display:flex;align-items:center;gap:6px}
  .app-dot{width:22px;height:22px;border-radius:50%;background:var(--app-cyan)}
  .app-name{font-size:20px;font-weight:500;color:var(--app-cyan)}

  .contact{position:absolute;display:flex;align-items:center;gap:8px;font-size:13.5px;white-space:nowrap}
  .contact svg{flex:none}
  .contact-web{left:398px;top:1129px}
  .contact-mail{left:620px;top:1129px}
  .contact-phone{left:472px;top:1161px;gap:10px}
  .contact-label{font-size:15px}
  .contact-number{font-size:21px;font-weight:700;margin-left:6px}
</style>
</head>
<body>
<main class="flyer">
  <div class="hero-photo" role="img" aria-label="Photo of an accountant at a desk marking printed bar and pie charts with a pen, glasses beside the papers"></div>
  <div class="brand-ring"></div>
  <div class="brand-name">KESTREL LEDGER</div>

  <section class="services-band">
    <h2 class="services-title">Services</h2>
    <div class="services-rule"></div>
  </section>

  <div class="service" style="left:19px;top:652px">
    <svg class="service-icon" viewBox="0 0 114 114"><circle cx="57" cy="57" r="57" fill="var(--purple)"/>
      <g fill="none" stroke="#fff" stroke-width="3" stroke-linejoin="round">
        <path d="M30 44 L88 34 L88 40 L30 50 Z"/><path d="M36 49 V88 H82 V40"/><path d="M36 36 V44"/>
        <rect x="48" y="72" width="14" height="14"/><rect x="62" y="72" width="14" height="14"/><rect x="55" y="58" width="14" height="14"/>
      </g></svg>
    <p class="service-label">Small Business Taxation</p>
  </div>
  <div class="service" style="left:294px;top:652px">
    <svg class="service-icon" viewBox="0 0 114 114"><circle cx="57" cy="57" r="57" fill="var(--pink)"/>
      <g fill="none" stroke="#fff" stroke-width="3" stroke-linejoin="round">
        <path d="M30 88 V24 L64 30 V88 Z"/><path d="M64 50 L84 56 V88 H64"/><path d="M42 88 V76 H52 V88"/>
        <path d="M38 40h4M46 40h4M54 40h4M38 50h4M46 50h4M54 50h4M38 60h4M46 60h4M54 60h4M72 64h6M72 72h6M72 80h6"/>
      </g></svg>
    <p class="service-label">Company &amp; Trust Tax Returns</p>
  </div>
  <div class="service" style="left:567px;top:652px">
    <svg class="service-icon" viewBox="0 0 114 114"><circle cx="57" cy="57" r="57" fill="var(--olive)"/>
      <g fill="none" stroke="#fff" stroke-width="3" stroke-linejoin="round">
        <path d="M50 42 L57 26 L64 42"/><rect x="22" y="42" width="70" height="40" rx="4"/>
      </g>
      <text x="57" y="69" text-anchor="middle" fill="#fff" font-family="Montserrat, sans-serif" font-weight="700" font-size="20" letter-spacing="2">RENT</text></svg>
    <p class="service-label">Rental Property Returns</p>
  </div>

  <div class="service" style="left:19px;top:869px">
    <svg class="service-icon" viewBox="0 0 114 114"><circle cx="57" cy="57" r="57" fill="var(--indigo)"/>
      <g fill="none" stroke="#fff" stroke-width="3" stroke-linejoin="round">
        <path d="M40 56 h14 l-3 8 c10 6 12 16 8 24 H30 c-4-8-2-18 8-24 Z"/>
        <rect x="58" y="60" width="20" height="28"/><rect x="64" y="40" width="20" height="20"/>
        <path d="M58 70h20M58 79h20M64 50h20M68 60v28M74 40v20"/>
      </g></svg>
    <p class="service-label">Capital Gains Tax</p>
  </div>
  <div class="service" style="left:294px;top:869px">
    <svg class="service-icon" viewBox="0 0 114 114"><circle cx="57" cy="57" r="57" fill="var(--royal)"/>
      <g fill="none" stroke="#fff" stroke-width="3" stroke-linecap="round">
        <circle cx="57" cy="48" r="9"/><path d="M42 86 V72 c0-8 6-13 15-13 s15 5 15 13 V86 Z"/>
        <path d="M28 50v4M28 62v4M28 74v4M86 50v4M86 62v4M86 74v4M48 30l2 3M57 27v4M66 30l-2 3M38 40l3 2M76 40l-3 2"/>
        <path d="M28 24v8M24 28h8M86 24v8M82 28h8"/>
      </g></svg>
    <p class="service-label">Individual Tax Returns</p>
  </div>
  <div class="service" style="left:567px;top:869px">
    <svg class="service-icon" viewBox="0 0 114 114"><circle cx="57" cy="57" r="57" fill="var(--green)"/>
      <g fill="none" stroke="#fff" stroke-width="3" stroke-linejoin="round">
        <path d="M57 86 L38 58 a22 22 0 1 1 38 0 Z"/><circle cx="57" cy="46" r="9"/>
      </g></svg>
    <p class="service-label">BAS and IAS lodgements</p>
  </div>

  <div class="footer-rule"></div>
  <div class="member-tab">Kestrel Ledger is a QLA Business</div>

  <div class="qla-mark"><span class="qla-square"></span><span class="qla-name">QLA</span></div>
  <div class="registered-badge"></div>
  <div class="app-partner"><span class="app-dot"></span><span class="app-name">Sumly</span></div>

  <div class="contact contact-web">
    <svg width="18" height="18" viewBox="0 0 20 20"><circle cx="10" cy="10" r="9" fill="var(--green)"/><path d="M5 6c3 0 4 2 3 4s1 4 0 6M12 3c0 3 3 3 5 4M13 12c2 0 3 2 2 4" stroke="#fff" stroke-width="1.6" fill="none"/></svg>
    <span>www.kestrelledger.com.au</span>
  </div>
  <div class="contact contact-mail">
    <svg width="18" height="14" viewBox="0 0 20 16"><rect x="1" y="1" width="18" height="14" fill="none" stroke="var(--teal)" stroke-width="2"/><path d="M1 1l9 8 9-8" fill="none" stroke="var(--teal)" stroke-width="2"/></svg>
    <span>hello@kestrelledger.com</span>
  </div>
  <div class="contact contact-phone">
    <svg width="24" height="24" viewBox="0 0 24 24"><path d="M5 2l4 1 1 5-3 2c1 3 3 5 6 6l2-3 5 1 1 4-3 3C10 22 2 14 2 5Z" fill="var(--teal)"/></svg>
    <span class="contact-label">Contact us</span><span class="contact-number">0400 555 018</span>
  </div>
</main>
</body>
</html>
```